E-learning Information & Community Website Needs a Makeover

I'm looking for a design makeover for my website "TavenNest.club". TavenNest's aim is to connect people to online learning through forums, information, guides & independent reviews. The site was launched in September 2014 using a forum software (Xenforo), but now needs a more polished and sophisticated look which communicates expertise and professionalism. I would like to see designs that use the current "TavenNest" blue (#0070c0). To visit the current website, go to http://www.tavennest.club/

Target Market(s)

People wishing to study online

Industry/Entity Type

Club

Number of Pages Required

4 page

Font styles to use
Sans Serif

Requirements
Must have
• A simple, clear and sophisticated lading page with links to the site's key features: discussion forums, Useful resources, Reviews, News etc, Articles. (See layout idea file attached)
• The main pages are the Landing Page, Discussion Forums, Resources & Reviews
• I would like to see designs that use the current "TavenNest" blue (#0070c0).
Nice to have
• Something uncluttered and easy to understand. The design should convey expertise in the field of online learning, giving users a sense of trust in the site's offerings.
• To give an idea of the sort of thing I'm after, take a look at brimvale.com website (screenshot attached)

```html
<!DOCTYPE html>
<html lang="en">
<head>
<meta charset="utf-8">
<title>TavenNest – Connecting People to Online Learning</title>
<link href="https://fonts.googleapis.com/css2?family=Open+Sans:wght@400;600;700&display=swap" rel="stylesheet">
<style>
:root{
  --brand:#0070c0;
  --brand-dark:#005da3;
  --nav:#a8c8e8;
  --green:#7ac943;
  --orange:#f7931e;
  --ink:#222;
  --muted:#666;
  --line:#e2e2e2;
  --panel:#f1f1f1;
  --footer:#f6f6f6;
}
*{box-sizing:border-box;margin:0;padding:0}
html,body{width:754px;height:1200px;overflow:hidden}
body{font-family:'Open Sans',sans-serif;color:var(--ink);background:#fff;position:relative}
.abs{position:absolute}

.site-header{top:0;left:0;width:754px;height:46px;background:var(--brand)}
.brand-name{left:60px;top:7px;color:#d7e9f7;font-size:18px;font-weight:400;letter-spacing:.2px;line-height:22px}
.brand-tag{left:60px;top:31px;color:#fff;font-size:7px;line-height:9px}
.btn-login{left:555px;top:15px;width:42px;height:16px;background:#0d3d6b;color:#fff;font-size:7px;font-weight:600;display:flex;align-items:center;justify-content:center}
.btn-signup{left:597px;top:15px;width:43px;height:16px;background:var(--green);color:#fff;font-size:7px;font-weight:600;display:flex;align-items:center;justify-content:center}
.lang{top:18px;width:14px;height:9px}
.lang-en{left:652px;background:linear-gradient(#b22 0 15%,#fff 15% 30%,#b22 30% 45%,#fff 45% 60%,#b22 60% 75%,#fff 75% 90%,#b22 90%)}
.lang-en::before{content:"";position:absolute;left:0;top:0;width:6px;height:5px;background:#3c3b6e}
.lang-es{left:670px;background:linear-gradient(#c60b1e 0 25%,#ffc400 25% 75%,#c60b1e 75%)}

.main-nav{top:46px;left:0;width:754px;height:31px;background:var(--nav);display:flex;align-items:center;padding-left:73px;gap:16px}
.main-nav a{font-size:7px;font-weight:600;color:#fff;text-decoration:none;text-transform:uppercase;white-space:nowrap}
.main-nav a.active{color:var(--brand)}

.hero{top:77px;left:0;width:754px;height:267px;background:radial-gradient(ellipse at 50% 40%,#fdfdfd 0%,#ececec 70%,#e4e4e4 100%)}
.hero-art{left:190px;top:23px;width:345px;height:150px;border-radius:70px;background:radial-gradient(ellipse at 50% 50%,rgba(0,112,192,.22),rgba(122,201,67,.12) 55%,rgba(255,255,255,0) 75%)}
.hero-arrow{top:124px}
.hero-title{left:0;width:754px;top:200px;text-align:center;font-size:9px;color:#555;text-transform:uppercase}
.hero-cta{left:313px;top:219px;width:128px;height:29px;background:var(--brand);color:#fff;font-size:9.5px;font-weight:700;display:flex;align-items:center;justify-content:center;border-radius:2px}

.feature{width:194px;height:101px;background:var(--brand);color:#fff;padding:17px 10px 0}
.feature h2{font-size:13px;font-weight:600;display:flex;align-items:center;gap:8px}
.feature h2 svg{width:11px;height:11px;fill:#fff;flex:none}
.feature p{font-size:7px;line-height:12px;margin-top:7px;color:#e8f2fb}
.feature .chip{display:inline-flex;align-items:center;justify-content:center;width:62px;height:18px;background:#fff;color:var(--brand);font-size:7px;font-weight:600;border-radius:2px;margin-top:9px}
.feature .field{margin-top:10px;height:18px;background:#1664a8;border:1px solid #2a78ba;color:#6fa6d3;font-size:6.5px;padding:4px 6px}

.divider{left:0;width:754px;height:1px;background:var(--line)}
.tag-label{left:72px;top:642px;width:59px;height:19px;background:var(--brand);color:#fff;font-size:9px;font-weight:600;display:flex;align-items:center;padding-left:18px;clip-path:polygon(0 0,88% 0,100% 50%,88% 100%,0 100%)}
.tag-text{left:143px;top:639px;width:520px;font-size:7px;line-height:13px;color:#333}

.community{top:678px;left:0;width:754px;height:463px;background:var(--panel)}
.community h3{position:absolute;top:22px;width:754px;text-align:center;font-size:13px;font-weight:600;color:#333}
.threads{position:absolute;left:71px;top:49px;width:614px;border-collapse:collapse;background:#fff;font-size:7px}
.threads th{background:linear-gradient(var(--brand),var(--brand-dark));color:#fff;height:32px;font-weight:600;font-size:7px;border-right:1px solid #2a82c9}
.threads th span{display:inline-flex;align-items:center;gap:6px}
.threads th svg{width:8px;height:8px;fill:#b9d6ee}
.threads td{height:43px;border:1px solid var(--line);text-align:center;color:#222}
.thread{display:flex;align-items:center;gap:7px;padding-left:6px;text-align:left}
.avatar{width:36px;height:34px;background:linear-gradient(#e9ecef,#b9a894);flex:none}
.badge{display:inline-block;background:var(--orange);color:#fff;font-size:6.5px;font-weight:600;padding:1px 8px;border-radius:2px}
.thread b{display:block;font-weight:400;font-size:7px;margin-top:2px}
.thread i{font-style:normal;color:#888;font-size:6.5px}

.site-footer{top:1141px;left:0;width:754px;height:59px;background:var(--footer)}
.foot-links{left:70px;top:17px;font-size:7.5px;color:#333}
.foot-links span{margin:0 5px;color:#555}
.copy{left:70px;top:36px;font-size:7.5px;color:#333}
.social{top:21px;width:19px;height:19px;border-radius:50%;border:1.5px solid #2d6fb3;background:#fff}
</style>
</head>
<body>

<header class="abs site-header">
  <div class="abs brand-name">TavenNest</div>
  <div class="abs brand-tag">Connecting People to Online Learning</div>
  <div class="abs btn-login">Login</div>
  <div class="abs btn-signup">Sign Up</div>
  <div class="abs lang lang-en" aria-label="English"></div>
  <div class="abs lang lang-es" aria-label="Español"></div>
</header>

<nav class="abs main-nav">
  <a class="active" href="#">Home</a><a href="#">Recent Activity</a><a href="#">What's New?</a><a href="#">Help</a><a href="#">Forums</a><a href="#">Resources</a><a href="#">Members</a><a href="#">FAQ</a><a href="#">Blog</a><a href="#">TavenNest Español</a><a href="#">Learning News</a>
</nav>

<section class="abs hero">
  <div class="abs hero-art" role="img" aria-label="Network of connected learner avatars in colourful circles"></div>
  <svg class="abs hero-arrow" style="left:51px" width="12" height="16" viewBox="0 0 12 16"><path d="M9 2 3 8l6 6" fill="none" stroke="#556" stroke-width="2"/></svg>
  <svg class="abs hero-arrow" style="left:691px" width="12" height="16" viewBox="0 0 12 16"><path d="m3 2 6 6-6 6" fill="none" stroke="#556" stroke-width="2"/></svg>
  <div class="abs hero-title">At the heart of connecting people to online learning</div>
  <div class="abs hero-cta">SIGN UP FOR FREE</div>
</section>

<article class="abs feature" style="left:70px;top:374px">
  <h2><svg viewBox="0 0 12 12"><circle cx="6" cy="6" r="6"/><path d="M3 6h5M6 3.5 8.5 6 6 8.5" stroke="#0070c0" stroke-width="1.5" fill="none"/></svg>Getting Started</h2>
  <p>Neque porro quisquam est qui dolorem ipsum quia dolor sit amet, consectetur, adipisci velit..</p>
  <span class="chip">Get Started</span>
</article>
<article class="abs feature" style="left:280px;top:374px">
  <h2><svg viewBox="0 0 12 12"><ellipse cx="5" cy="5" rx="5" ry="3.5"/><ellipse cx="8" cy="8" rx="4" ry="3"/></svg>Discussions</h2>
  <p>Neque porro quisquam est qui dolorem ipsum quia dolor sit amet, consectetur, adipisci velit..</p>
  <span class="chip">Discussions</span>
</article>
<article class="abs feature" style="left:490px;top:374px">
  <h2><svg viewBox="0 0 12 12"><path d="M6 0l1.8 4 4.2.4-3.2 2.8 1 4.2L6 9.2 2.2 11.4l1-4.2L0 4.4 4.2 4z"/></svg>Reviews</h2>
  <p>Neque porro quisquam est qui dolorem ipsum quia dolor sit amet, consectetur, adipisci velit..</p>
  <span class="chip">Get Reviews</span>
</article>
<article class="abs feature" style="left:70px;top:498px">
  <h2><svg viewBox="0 0 12 12"><rect x=".7" y="2" width="9" height="9" fill="none" stroke="#fff" stroke-width="1.4"/><path d="M3 6l2 2 6-7" fill="none" stroke="#fff" stroke-width="1.6"/></svg>Tips &amp; Guidelines</h2>
  <p>Neque porro quisquam est qui dolorem ipsum quia dolor sit amet, consectetur, adipisci velit..</p>
  <span class="chip">Get Started</span>
</article>
<article class="abs feature" style="left:280px;top:498px">
  <h2><svg viewBox="0 0 12 12"><path d="M2 0h5l3 3v9H2z"/><path d="M4 6h4M4 8h4" stroke="#0070c0"/></svg>News &amp; Articles</h2>
  <p>Neque porro quisquam est qui dolorem ipsum quia dolor sit amet, consectetur, adipisci velit..</p>
  <span class="chip">Discussions</span>
</article>
<article class="abs feature" style="left:490px;top:498px">
  <h2><svg viewBox="0 0 12 12"><rect x=".7" y="2" width="10.6" height="8" fill="none" stroke="#fff" stroke-width="1.4"/><path d="M1 2.5l5 4 5-4" fill="none" stroke="#fff" stroke-width="1.3"/></svg>Newsletter</h2>
  <div class="field">Enter Your E-mail ID</div>
  <span class="chip">Subscribe</span>
</article>

<div class="abs divider" style="top:625px"></div>
<div class="abs tag-label">TAGS</div>
<p class="abs tag-text">Lorem Ipsum, simply dummy text , printing and typesetting industry, Lorem Ipsum, Has been the industry's, standard dummy text ever since the 1500s, when an unknown, printer took a galley, type and scrambled , Make a type, specimen book.</p>

<section class="abs community">
  <h3>From The Community</h3>
  <table class="threads">
    <colgroup><col style="width:156px"><col style="width:98px"><col style="width:98px"><col style="width:98px"><col style="width:164px"></colgroup>
    <thead><tr>
      <th><span><svg viewBox="0 0 8 8"><path d="M0 0h4l4 4-4 4-4-4z"/></svg>Recent Threads</span></th>
      <th><span><svg viewBox="0 0 8 8"><rect width="8" height="8"/></svg>Start Date</span></th>
      <th><span><svg viewBox="0 0 8 8"><path d="M3 0 0 3l3 3V4c3 0 4 1 5 4 0-4-2-6-5-6z"/></svg>Replies</span></th>
      <th><span><svg viewBox="0 0 8 8"><ellipse cx="4" cy="4" rx="4" ry="2.5"/></svg>View</span></th>
      <th><span><svg viewBox="0 0 8 8"><rect y="1" width="8" height="6"/></svg>Last Message</span></th>
    </tr></thead>
    <tbody>
      <tr><td><div class="thread"><div class="avatar" role="img" aria-label="Member avatar"></div><div><span class="badge">Courses</span><b>Orbit MOOCs</b><i>Marisol</i></div></div></td><td>20 - 5- 2015</td><td>0</td><td>25</td><td>Marisol , Today at 9:30 AM</td></tr>
      <tr><td><div class="thread"><div class="avatar" role="img" aria-label="Member avatar"></div><div><span class="badge">Courses</span><b>Orbit MOOCs</b><i>Marisol</i></div></div></td><td>20 - 5- 2015</td><td>0</td><td>25</td><td>Marisol , Today at 9:30 AM</td></tr>
      <tr><td><div class="thread"><div class="avatar" role="img" aria-label="Member avatar"></div><div><span class="badge">Courses</span><b>Orbit MOOCs</b><i>Marisol</i></div></div></td><td>20 - 5- 2015</td><td>0</td><td>25</td><td>Marisol , Today at 9:30 AM</td></tr>
      <tr><td><div class="thread"><div class="avatar" role="img" aria-label="Member avatar"></div><div><span class="badge">Courses</span><b>Orbit MOOCs</b><i>Marisol</i></div></div></td><td>20 - 5- 2015</td><td>0</td><td>25</td><td>Marisol , Today at 9:30 AM</td></tr>
      <tr><td><div class="thread"><div class="avatar" role="img" aria-label="Member avatar"></div><div><span class="badge">Courses</span><b>Orbit MOOCs</b><i>Marisol</i></div></div></td><td>20 - 5- 2015</td><td>0</td><td>25</td><td>Marisol , Today at 9:30 AM</td></tr>
      <tr><td><div class="thread"><div class="avatar" role="img" aria-label="Member avatar"></div><div><span class="badge">Courses</span><b>Orbit MOOCs</b><i>Marisol</i></div></div></td><td>20 - 5- 2015</td><td>0</td><td>25</td><td>Marisol , Today at 9:30 AM</td></tr>
      <tr><td><div class="thread"><div class="avatar" role="img" aria-label="Member avatar"></div><div><span class="badge">Courses</span><b>Orbit MOOCs</b><i>Marisol</i></div></div></td><td>20 - 5- 2015</td><td>0</td><td>25</td><td>Marisol , Today at 9:30 AM</td></tr>
      <tr><td><div class="thread"><div class="avatar" role="img" aria-label="Member avatar"></div><div><span class="badge">Courses</span><b>Orbit MOOCs</b><i>Marisol</i></div></div></td><td>20 - 5- 2015</td><td>0</td><td>25</td><td>Marisol , Today at 9:30 AM</td></tr>
    </tbody>
  </table>
</section>

<footer class="abs site-footer">
  <div class="abs foot-links">About<span>|</span>Contact Us<span>|</span>Help<span>|</span>Home<span>|</span>FAQ<span>|</span>Community Guidelines<span>|</span>Top</div>
  <div class="abs copy">© 2015 Company Name, All Rights Reserved</div>
  <div class="abs social" style="left:577px" aria-label="Social link"></div>
  <div class="abs social" style="left:599px" aria-label="Social link"></div>
  <div class="abs social" style="left:621px" aria-label="Social link"></div>
  <div class="abs social" style="left:643px" aria-label="Social link"></div>
  <div class="abs social" style="left:666px" aria-label="Social link"></div>
</footer>

</body>
</html>
```